Maison Orvelle
Maison Orvelle - Architecture
Creative Brief
Professional
Corinne Valcourt, B.ID.,OFM.,RVUPO., PRQF., WLGH
Owner/ Principal Designer
87 Larchmere Dr Vaughan, Ontario L4K 3J9 -------------------------------------------- 382 Brindle Row, Suite 4-7160 Valley Cottage, NY 10982
corinnevalcourt@maisonorvelle.com
www.maisonorvelle.com
The emails address to be add on my card are: corinnevalcourt@maisonorvelle.com, hello@maisonorvelle.com And I also need an additional card with a different name on it: Name: Glen Hartwick, B Arch,Sci.,CET Title: Owner/Project Manager Address: the same as above Phone: 416.555.0148, 845.555.0173 Email: glen@maisonorvelle.com hello@maisonorvelle.com Web: www.maisonorvelle.com I would like to have the card black, white writing and some silver.
I want to see the logo also on the back of the card. Services: .Professional Interior Design & Architecture .Design Build & Remodeling .Design Concept & Development .Project Management .Decor & Styling .Consultations

```html
<!DOCTYPE html>
<html lang="en">
<head>
<meta charset="utf-8">
<title>Maison Orvelle – Business Card</title>
<link rel="stylesheet" href="https://fonts.googleapis.com/css2?family=Raleway:wght@300;400;500&display=swap">
<style>
  :root {
    --page: #ffffff;
    --card-dark: #2e2e2e;
    --card-mid: #4a4a4a;
    --ink: #f2f2f2;
    --silver: #c9c9c9;
    --silver-soft: #9a9a9a;
    --rule: #d8d8d8;
  }
  * { margin: 0; padding: 0; box-sizing: border-box; }
  html, body {
    width: 1200px; height: 360px; overflow: hidden;
    background: var(--page);
    font-family: "Raleway", "Helvetica Neue", Arial, sans-serif;
    color: var(--ink);
  }
  .sheet { position: relative; width: 1200px; height: 360px; }
  .card {
    position: absolute; top: 0; width: 583px; height: 360px; overflow: hidden;
    background: radial-gradient(ellipse at 30% 35%, var(--card-mid) 0%, var(--card-dark) 75%);
  }
  .card--front { left: 0; }
  .card--back { left: 617px; }
  .abs { position: absolute; white-space: nowrap; }

  /* front */
  .front-mark { left: 80px; top: 60px; }
  .front-wordmark {
    left: 14px; top: 152px; width: 190px; text-align: center;
    font-size: 18px; font-weight: 400; letter-spacing: 3.5px; color: var(--ink);
  }
  .front-wave { left: 0; top: 210px; }
  .person { right: 14px; top: 124px; text-align: right; }
  .person__name { font-size: 19px; font-weight: 400; line-height: 24px; }
  .person__creds { font-size: 13px; font-weight: 400; margin-top: 6px; letter-spacing: .3px; line-height: 16px; }
  .person__rule { height: 2px; background: var(--rule); width: 200px; margin: 6px 0 6px auto; }
  .person__title { font-size: 14px; font-weight: 400; line-height: 18px; }

  .contact { font-size: 14px; line-height: 24px; color: var(--ink); }
  .contact--phone { left: 14px; top: 280px; }
  .contact--mail { left: 276px; top: 296px; }
  .contact__row { display: flex; align-items: center; gap: 8px; }
  .contact__icon { width: 14px; flex: none; }
  .contact__indent { padding-left: 22px; }

  /* back */
  .back-mark { left: 252px; top: 62px; }
  .back-wordmark {
    left: 0; width: 583px; top: 160px; text-align: center;
    font-size: 30px; font-weight: 300; letter-spacing: 8px; color: var(--silver);
  }
  .back-web {
    left: 0; width: 583px; top: 200px; text-align: center;
    font-size: 15px; font-weight: 500; color: var(--ink); letter-spacing: .4px;
  }
  .addresses { left: 150px; top: 244px; width: 350px; text-align: center; font-size: 13px; }
  .addresses__rule { height: 1px; background: var(--rule); }
  .addresses__line { padding: 9px 0; }
</style>
</head>
<body>
<main class="sheet">

  <section class="card card--front" aria-label="Card front">
    <svg class="abs front-mark" width="64" height="64" viewBox="0 0 64 64" aria-hidden="true">
      <circle cx="32" cy="32" r="29" fill="none" stroke="var(--ink)" stroke-width="3"/>
    </svg>
    <div class="abs front-wordmark">MAISON ORVELLE</div>

    <svg class="abs front-wave" width="583" height="60" viewBox="0 0 583 60" aria-hidden="true">
      <path d="M0 52 C150 10 300 4 420 14 S540 24 583 20" fill="none" stroke="var(--silver)" stroke-width="2.2" opacity=".9"/>
      <path d="M0 58 C160 22 310 16 430 24 S545 32 583 28" fill="none" stroke="var(--silver-soft)" stroke-width="1" opacity=".7"/>
    </svg>

    <div class="abs person">
      <div class="person__name">Corinne Valcourt</div>
      <div class="person__creds">B.ID.,OFM.,RVUPO.,PRQF., WLGH</div>
      <div class="person__rule"></div>
      <div class="person__title">Owner/ Principal Designer</div>
    </div>

    <div class="abs contact contact--phone">
      <div class="contact__row">
        <svg class="contact__icon" viewBox="0 0 14 14" aria-hidden="true">
          <path d="M3 1 L5 1 L6 4 L4.5 5.2 C5.3 7 7 8.7 8.8 9.5 L10 8 L13 9 L13 11 C13 12 12 13 11 13 C6 12.5 1.5 8 1 3 C1 2 2 1 3 1Z" fill="var(--ink)"/>
        </svg>
        <span>416.555.0148,</span>
      </div>
      <div class="contact__indent">845.555.0173</div>
    </div>

    <div class="abs contact contact--mail">
      <div class="contact__row">
        <svg class="contact__icon" viewBox="0 0 14 10" aria-hidden="true">
          <rect x="0" y="0" width="14" height="10" fill="var(--ink)"/>
          <path d="M0 0 L7 6 L14 0" fill="none" stroke="var(--card-dark)" stroke-width="1.2"/>
        </svg>
        <span>corinnevalcourt@maisonorvelle.com</span>
      </div>
      <div class="contact__indent">hello@maisonorvelle.com</div>
    </div>
  </section>

  <section class="card card--back" aria-label="Card back">
    <svg class="abs back-mark" width="80" height="80" viewBox="0 0 80 80" aria-hidden="true">
      <circle cx="40" cy="40" r="36" fill="none" stroke="var(--silver)" stroke-width="4"/>
    </svg>
    <div class="abs back-wordmark">MAISON ORVELLE</div>
    <div class="abs back-web">www.maisonorvelle.com</div>

    <div class="abs addresses">
      <div class="addresses__rule"></div>
      <div class="addresses__line">87 Larchmere Dr Vaughan, Ontario L4K 3J9</div>
      <div class="addresses__rule"></div>
      <div class="addresses__line">382 Brindle Row, Suite 4-7160 Valley Cottage, NY 10982</div>
    </div>
  </section>

</main>
</body>
</html>
```